Talvex Industrial Maintenance Business Card

Design a business card with the following information, logo must be included.
Talvex Industrial Maintenance
Dale Virnow Jr.
Pone 413-627-8154
email dale.virnow.jr@brindlemail.net

```html
<!DOCTYPE html>
<html lang="en">
<head>
<meta charset="utf-8">
<title>Talvex Industrial Maintenance – Business Card</title>
<link href="https://fonts.googleapis.com/css2?family=Montserrat:wght@500;600&display=swap" rel="stylesheet">
<style>
  :root {
    --backdrop: #b3b3b3;
    --brand-blue: #0071bc;
    --steel-grey: #808080;
    --ink: #333333;
    --paper: #ffffff;
  }
  * { margin: 0; padding: 0; box-sizing: border-box; }
  html, body { width: 1000px; height: 1200px; overflow: hidden; }
  body { background: var(--backdrop); position: relative; font-family: "Montserrat", sans-serif; }

  .card { position: absolute; left: 51px; width: 898px; height: 539px; overflow: hidden; }
  .card-front { top: 44px; background: var(--paper); }
  .card-back { top: 617px; background: var(--paper); }

  .decor { position: absolute; inset: 0; }

  .band { position: absolute; left: 0; width: 100%; }
  .front-band-top { top: 0; height: 39px; background: var(--brand-blue); }
  .front-band-bottom { bottom: 0; height: 39px; background: var(--steel-grey); }
  .back-field { top: 40px; height: 458px; background: var(--brand-blue); }

  .brand { position: absolute; display: flex; align-items: center; font-weight: 600; }
  .brand-dot { border-radius: 50%; flex: none; }
  .brand-name { display: flex; flex-direction: column; line-height: 1; text-transform: uppercase; }
  .brand-main { letter-spacing: 1px; }

  .brand-front { left: 68px; top: 80px; color: var(--brand-blue); }
  .brand-front .brand-dot { width: 100px; height: 100px; background: var(--brand-blue); margin-right: 20px; }
  .brand-front .brand-main { font-size: 61px; }
  .brand-front .brand-sub { font-size: 17px; margin-top: 6px; }

  .brand-back { left: 228px; top: 212px; color: var(--paper); }
  .brand-back .brand-dot { width: 114px; height: 114px; background: var(--paper); margin-right: 23px; }
  .brand-back .brand-main { font-size: 68px; }
  .brand-back .brand-sub { font-size: 19px; margin-top: 6px; }

  .contact { position: absolute; left: 503px; top: 348px; color: var(--ink); }
  .contact-name { font-size: 28px; font-weight: 500; margin-bottom: 14px; }
  .contact-line { display: flex; align-items: center; font-size: 21px; font-weight: 500; height: 26px; margin-bottom: 14px; }
  .contact-icon { width: 26px; height: 26px; background: var(--brand-blue); border-radius: 3px; margin-right: 9px; display: flex; align-items: center; justify-content: center; }
</style>
</head>
<body>

<section class="card card-front" aria-label="Card front">
  <svg class="decor" width="898" height="539" viewBox="0 0 898 539" aria-hidden="true">
    <circle cx="846" cy="41" r="156" fill="none" stroke="var(--brand-blue)" stroke-width="43"/>
    <circle cx="104" cy="473" r="195" fill="none" stroke="var(--steel-grey)" stroke-width="51"/>
  </svg>
  <div class="band front-band-top"></div>
  <div class="band front-band-bottom"></div>

  <div class="brand brand-front">
    <span class="brand-dot"></span>
    <span class="brand-name">
      <span class="brand-main">Talvex</span>
      <span class="brand-sub">Industrial Maintenance</span>
    </span>
  </div>

  <div class="contact">
    <p class="contact-name">Dale Virnow Jr.</p>
    <p class="contact-line">
      <span class="contact-icon">
        <svg width="16" height="16" viewBox="0 0 24 24" aria-hidden="true"><path fill="#fff" d="M6.6 10.8a15.1 15.1 0 0 0 6.6 6.6l2.2-2.2a1 1 0 0 1 1-.25 11.4 11.4 0 0 0 3.6.57 1 1 0 0 1 1 1V20a1 1 0 0 1-1 1A17 17 0 0 1 3 4a1 1 0 0 1 1-1h3.5a1 1 0 0 1 1 1c0 1.25.2 2.45.57 3.57a1 1 0 0 1-.25 1z"/></svg>
      </span>
      413-627-8154
    </p>
    <p class="contact-line">
      <span class="contact-icon">
        <svg width="18" height="14" viewBox="0 0 18 14" aria-hidden="true"><rect x="1" y="1" width="16" height="12" fill="none" stroke="#fff" stroke-width="1.5"/><path d="M1 1l8 7 8-7M1 13l6-6M17 13l-6-6" fill="none" stroke="#fff" stroke-width="1.3"/></svg>
      </span>
      dale.virnow.jr@brindlemail.net
    </p>
  </div>
</section>

<section class="card card-back" aria-label="Card back">
  <div class="band back-field"></div>
  <svg class="decor" width="898" height="539" viewBox="0 0 898 539" aria-hidden="true">
    <circle cx="76" cy="26" r="146" fill="none" stroke="var(--paper)" stroke-width="38"/>
    <circle cx="830" cy="500" r="167" fill="none" stroke="var(--paper)" stroke-width="46"/>
  </svg>

  <div class="brand brand-back">
    <span class="brand-dot"></span>
    <span class="brand-name">
      <span class="brand-main">Talvex</span>
      <span class="brand-sub">Industrial Maintenance</span>
    </span>
  </div>
</section>

</body>
</html>
```